WordPress Website Design Project

Technical & Functional Deliverables
WordPress CMS
Fully responsive design
Integrated WhatsApp chatbot
Custom article filtering system
SEO-friendly site structure & performance optimization
CMS user manual & training session
Updates

Need extra days to review

Industry/Entity Type

Industrial Safety and Compliance

Coding

Coded - Design and coding required

Number of Pages Required

5+ page

Font styles to use
Sans Serif

Colors
0054AA
0677BA
7BADD7
CADEEF
E8F1F8

```html
<!DOCTYPE html>
<html lang="en">
<head>
<meta charset="utf-8">
<title>Ostrevo — Industrial Safety &amp; Compliance</title>
<link href="https://fonts.googleapis.com/css2?family=Montserrat:wght@400;500;600;700;800&display=swap" rel="stylesheet">
<style>
:root{
  --navy:#1f3152;
  --navy-deep:#1a2a47;
  --blue:#0054AA;
  --mid:#0677BA;
  --accent:#5b8fd0;
  --sky:#7BADD7;
  --pale:#CADEEF;
  --mist:#E8F1F8;
  --ink:#1e2433;
  --text:#3a4150;
  --white:#ffffff;
}
*{box-sizing:border-box;margin:0;padding:0}
html,body{width:1200px;height:5063px;overflow:hidden}
body{font-family:"Montserrat",sans-serif;color:var(--ink);background:var(--white);position:relative}
section,header,footer{position:absolute;left:0;width:1200px}

/* header */
.site-header{top:0;height:116px;background:var(--white)}
.brand{position:absolute;display:flex;align-items:center;gap:10px;font-weight:700;color:var(--navy);letter-spacing:2px;white-space:nowrap}
.brand .mark{display:block;background:var(--accent)}
.site-header .brand{left:68px;top:28px;font-size:48px}
.site-header .brand .mark{width:58px;height:62px}
.nav{position:absolute;left:490px;top:48px;display:flex;align-items:center;font-size:13px;color:var(--ink);font-weight:500}
.nav a{text-decoration:none;color:inherit;padding:2px 10px}
.nav .active{background:var(--accent);color:var(--white)}
.nav .sep{margin:0 16px;font-size:15px}
.btn-head{position:absolute;left:1011px;top:35px;width:123px;height:47px;background:var(--navy);color:var(--white);font-size:13px;font-weight:500;display:flex;align-items:center;justify-content:center}

/* hero */
.hero{top:116px;height:699px;background:linear-gradient(90deg,#24395e 0%,#2b4470 55%,#1f3152 72%)}
.hero-right{position:absolute;left:858px;top:0;width:342px;height:699px;background:var(--navy-deep)}
.hero .kicker{position:absolute;left:68px;top:130px;font-size:36px;font-weight:600;color:var(--accent)}
.hero h1{position:absolute;left:66px;top:180px;font-size:72px;line-height:86px;font-weight:800;color:var(--white)}
.hero h1 span{color:var(--accent)}
.btn-outline{position:absolute;left:68px;top:476px;width:304px;height:80px;border:3px solid var(--white);color:var(--white);font-size:26px;font-weight:600;display:flex;align-items:center;padding-left:42px;gap:38px}
.btn-outline i{display:block;width:32px;height:32px;background:var(--accent)}
.hero-block{position:absolute;left:995px;top:420px;width:205px;height:194px;background:var(--white)}
.hero-frame{position:absolute;left:612px;top:120px;width:531px;height:454px;border:3px solid var(--white)}
.hero-photo{position:absolute;left:622px;top:130px;width:511px;height:434px;background:linear-gradient(135deg,#5f7896,#9fb3c7 45%,#3d4f66)}

/* section heading */
.ornament{position:absolute;left:0;width:1200px;display:flex;justify-content:center;align-items:center;gap:8px}
.ornament b{display:block;width:48px;height:3px;background:var(--accent)}
.ornament i{display:block;width:26px;height:26px;background:var(--accent)}
.sec-title{position:absolute;left:0;width:1200px;text-align:center;font-size:53px;font-weight:700;color:var(--navy)}

/* values */
.values{top:815px;height:985px}
.values .lead{position:absolute;width:1200px;top:250px;text-align:center;font-size:22px;font-weight:500}
.values .sub{position:absolute;width:1200px;top:290px;text-align:center;font-size:22px;font-weight:600;color:var(--accent)}
.values .mission{position:absolute;left:160px;width:880px;top:338px;text-align:center;font-size:13px;line-height:26px;color:var(--text)}
.values-frame{position:absolute;left:132px;top:453px;width:413px;height:424px;border:2px solid var(--accent)}
.values-photo{position:absolute;left:150px;top:470px;width:412px;height:430px;background:linear-gradient(160deg,#6d7480,#b9a889 50%,#4b5565)}
.values h3{position:absolute;left:620px;top:488px;font-size:19px;line-height:32px;font-weight:700;color:var(--ink)}
.value-list{position:absolute;left:622px;top:575px;list-style:none;width:460px}
.value-list li{position:relative;padding-left:36px;font-size:15px;line-height:19px;color:var(--text);margin-bottom:15px}
.value-list li b{color:var(--ink)}
.value-list svg{position:absolute;left:0;top:2px}

/* work */
.work{top:1800px;height:930px;background:var(--mist)}
.card-work{position:absolute;top:250px;width:347px}
.card-work .photo{height:288px;border-radius:6px}
.card-work h4{margin:30px 5px 0;font-size:23px;line-height:30px;font-weight:600;color:var(--ink)}
.card-work p{margin:18px 5px 0;font-size:13px;line-height:24px;color:var(--text)}
.btn-more{display:flex;align-items:center;gap:14px;margin:22px 5px 0;width:168px;height:42px;background:var(--accent);color:var(--white);font-size:14px;font-weight:600;padding-left:20px}
.dots{position:absolute;left:0;width:1200px;display:flex;justify-content:center;gap:10px;align-items:center}
.dots i{display:block;width:9px;height:9px;border-radius:50%;background:var(--pale)}
.dots i.on{width:24px;height:6px;border-radius:3px;background:var(--accent)}

/* clients */
.clients{top:2730px;height:460px}
.arrow-btn{position:absolute;top:270px;width:42px;height:38px;display:flex;align-items:center;justify-content:center}
.client{position:absolute;top:238px;width:178px;height:97px;background:var(--white);border-radius:8px;box-shadow:0 4px 16px rgba(30,50,90,.14);display:flex;align-items:center;justify-content:center;font-size:15px;font-weight:700;color:var(--navy);white-space:nowrap}

/* solutions */
.solutions{top:3190px;height:750px;background:var(--mist)}
.sol{position:absolute;top:260px;width:255px;height:380px;border-radius:8px;overflow:hidden}
.sol .photo{position:absolute;inset:0}
.sol .cap{position:absolute;left:0;right:0;bottom:0;height:78px;background:rgba(31,49,82,.55);color:var(--white);font-size:18px;line-height:22px;font-weight:500;text-align:center;display:flex;align-items:center;justify-content:center;padding:0 12px}

/* people */
.people{top:3940px;height:800px}
.person{position:absolute;top:255px;width:253px}
.person .photo{height:330px}
.person .plate{margin:-12px auto 0;width:215px;height:44px;background:var(--white);box-shadow:0 3px 10px rgba(30,50,90,.14);text-align:center;position:relative}
.person .plate b{display:block;font-size:15px;font-weight:700;padding-top:6px;color:var(--ink)}
.person .plate span{display:block;font-size:11px;color:var(--text)}

/* footer */
.site-footer{top:4740px;height:323px;background:var(--navy)}
.site-footer .about{position:absolute;left:215px;top:68px;font-size:16px;line-height:26px;color:var(--white)}
.foot-links{position:absolute;left:803px;top:58px;list-style:none}
.foot-links li{font-size:13px;line-height:26px;color:var(--white);display:flex;align-items:center;gap:8px}
.foot-links li i{display:block;width:8px;height:8px;background:var(--sky)}
.site-footer hr{position:absolute;left:68px;top:208px;width:1065px;border:0;border-top:1px solid rgba(255,255,255,.35)}
.legal{position:absolute;left:68px;top:250px;font-size:13px;color:var(--white)}
.social{position:absolute;left:68px;top:280px;width:22px;height:22px;border-radius:50%;background:var(--accent)}
.copy{position:absolute;left:480px;top:264px;font-size:13px;color:var(--white)}
.site-footer .brand{left:842px;top:240px;font-size:48px;color:var(--white)}
.site-footer .brand .mark{width:58px;height:62px}
</style>
</head>
<body>

<header class="site-header">
  <div class="brand"><span class="mark"></span>OSTREVO</div>
  <nav class="nav">
    <a class="active">HOME</a><span class="sep">|</span>
    <a>ABOUT US</a><span class="sep">|</span>
    <a>SOLUTIONS</a><span class="sep">|</span>
    <a>ARTICLES</a>
  </nav>
  <div class="btn-head">CONTACT US</div>
</header>

<section class="hero">
  <div class="hero-right"></div>
  <div class="kicker">Your Partner In</div>
  <h1>INDUSTRIAL<br>SAFETY &amp;<br><span>Compliance</span></h1>
  <div class="btn-outline">CONTACT US <i></i></div>
  <div class="hero-block"></div>
  <div class="hero-frame"></div>
  <div class="hero-photo" role="img" aria-label="Two engineers in a control room, one in a hard hat, reviewing equipment on a laptop"></div>
</section>

<section class="values">
  <div class="ornament" style="top:115px"><b></b><i></i><b></b></div>
  <h2 class="sec-title" style="top:145px">OUR VALUES</h2>
  <p class="lead">We are Ostrevo: Your Partner in Industrial Safety and Compliance.</p>
  <p class="sub">Mission Statement and Core Values</p>
  <p class="mission">To provide expert guidance and practical solutions in industrial safety and compliance, delivering clarity, reliability, and peace<br>of mind to every partner we serve.</p>
  <div class="values-frame"></div>
  <div class="values-photo" role="img" aria-label="Engineer in a yellow hard hat reading plans in front of industrial pipework"></div>
  <h3>WE ACHIEVE THIS MISSION BY STAYING<br>TRUE TO OUR FOUNDATIONAL VALUES:</h3>
  <ul class="value-list">
    <li><svg width="20" height="20"><circle cx="10" cy="10" r="10" fill="#5b8fd0"/><path d="M5.5 10.2l3 3 6-6" stroke="#fff" stroke-width="2" fill="none"/></svg><b>ASSURANCE:</b> Providing confidence through technically robust solutions.</li>
    <li><svg width="20" height="20"><circle cx="10" cy="10" r="10" fill="#5b8fd0"/><path d="M5.5 10.2l3 3 6-6" stroke="#fff" stroke-width="2" fill="none"/></svg><b>RELIABILITY:</b> Ensuring consistent performance in demanding situations.</li>
    <li><svg width="20" height="20"><circle cx="10" cy="10" r="10" fill="#5b8fd0"/><path d="M5.5 10.2l3 3 6-6" stroke="#fff" stroke-width="2" fill="none"/></svg><b>COMMITMENT:</b> Fulfilling promises and exceeding expectations.</li>
    <li><svg width="20" height="20"><circle cx="10" cy="10" r="10" fill="#5b8fd0"/><path d="M5.5 10.2l3 3 6-6" stroke="#fff" stroke-width="2" fill="none"/></svg><b>HONOR:</b> Upholding the highest ethical standards.</li>
    <li><svg width="20" height="20"><circle cx="10" cy="10" r="10" fill="#5b8fd0"/><path d="M5.5 10.2l3 3 6-6" stroke="#fff" stroke-width="2" fill="none"/></svg><b>EXPERTISE:</b> Leveraging deep industry knowledge to solve complex challenges.</li>
    <li><svg width="20" height="20"><circle cx="10" cy="10" r="10" fill="#5b8fd0"/><path d="M5.5 10.2l3 3 6-6" stroke="#fff" stroke-width="2" fill="none"/></svg><b>RESPONSIBILITY:</b> Taking full accountability from concept through completion.</li>
  </ul>
</section>

<section class="work">
  <div class="ornament" style="top:110px"><b></b><i></i><b></b></div>
  <h2 class="sec-title" style="top:140px">OUR WORK</h2>
  <article class="card-work" style="left:68px">
    <div class="photo" role="img" aria-label="Two workers in orange hard hats assembling machinery" style="background:linear-gradient(135deg,#3a5068,#b8764a 55%,#2c3a4c)"></div>
    <h4>Lorem ipsum dolor sit amet ipsum dolor</h4>
    <p>Lorem ipsum dolor sit amet, consectetur adip iscing elit. Praesent erat sem, placerat .</p>
    <div class="btn-more">READ MORE <svg width="30" height="12"><path d="M0 6h27M22 1l6 5-6 5" stroke="#fff" stroke-width="2" fill="none"/></svg></div>
  </article>
  <article class="card-work" style="left:430px">
    <div class="photo" role="img" aria-label="Engineer holding a tablet projecting a holographic building model" style="background:linear-gradient(135deg,#1e3c5c,#3f86b8 55%,#c79a5a)"></div>
    <h4>Lorem ipsum dolor sit amet ipsum dolor</h4>
    <p>Lorem ipsum dolor sit amet, consectetur adip iscing elit. Praesent erat sem, placerat .</p>
    <div class="btn-more">READ MORE <svg width="30" height="12"><path d="M0 6h27M22 1l6 5-6 5" stroke="#fff" stroke-width="2" fill="none"/></svg></div>
  </article>
  <article class="card-work" style="left:790px">
    <div class="photo" role="img" aria-label="Two workers in hard hats reviewing plans in front of a refinery" style="background:linear-gradient(160deg,#8fb3d3,#d9c59a 50%,#6f8a4a)"></div>
    <h4>Lorem ipsum dolor sit amet ipsum dolor</h4>
    <p>Lorem ipsum dolor sit amet, consectetur adip iscing elit. Praesent erat sem, placerat .</p>
    <div class="btn-more">READ MORE <svg width="30" height="12"><path d="M0 6h27M22 1l6 5-6 5" stroke="#fff" stroke-width="2" fill="none"/></svg></div>
  </article>
  <div class="dots" style="top:828px"><i class="on"></i><i></i><i></i><i></i></div>
</section>

<section class="clients">
  <div class="ornament" style="top:110px"><b></b><i></i><b></b></div>
  <h2 class="sec-title" style="top:140px">OUR CLIENTS</h2>
  <div class="arrow-btn" style="left:55px;background:var(--accent)"><svg width="16" height="12"><path d="M15 6H2M6 1L1 6l5 5" stroke="#fff" stroke-width="2" fill="none"/></svg></div>
  <div class="client" style="left:140px">Kestrel</div>
  <div class="client" style="left:325px">Fieldhaus</div>
  <div class="client" style="left:510px">Orlin</div>
  <div class="client" style="left:695px">Marrow</div>
  <div class="client" style="left:880px">Trellis Consulting</div>
  <div class="arrow-btn" style="left:1100px;background:var(--navy)"><svg width="16" height="12"><path d="M1 6h13M10 1l5 5-5 5" stroke="#fff" stroke-width="2" fill="none"/></svg></div>
</section>

<section class="solutions">
  <div class="ornament" style="top:115px"><b></b><i></i><b></b></div>
  <h2 class="sec-title" style="top:145px">OUR SOLUTIONS</h2>
  <div class="sol" style="left:70px"><div class="photo" role="img" aria-label="Workers in a plant with pipes and machinery" style="background:linear-gradient(160deg,#5e6b7a,#b78a4a 60%,#2f3b4b)"></div><div class="cap">Engineering &amp; design</div></div>
  <div class="sol" style="left:338px"><div class="photo" role="img" aria-label="Technician in a hard hat facing a server and data display" style="background:linear-gradient(160deg,#a8b6c4,#3d6a92 55%,#1e3552)"></div><div class="cap">Technical Support &amp;<br>Site Services</div></div>
  <div class="sol" style="left:608px"><div class="photo" role="img" aria-label="Two workers in white hard hats checking equipment" style="background:linear-gradient(160deg,#c4cdd6,#3e5f9a 55%,#b54a3a)"></div><div class="cap">Risk Management &amp;<br>Compliance Services</div></div>
  <div class="sol" style="left:878px"><div class="photo" role="img" aria-label="Worker in a yellow hard hat using a handheld device in a factory" style="background:linear-gradient(160deg,#6d8bb0,#b7c2cc 50%,#3a4d6a)"></div><div class="cap">Transitioning to<br>Fluorine-Free Foam</div></div>
</section>

<section class="people">
  <div class="ornament" style="top:110px"><b></b><i></i><b></b></div>
  <h2 class="sec-title" style="top:140px">OUR PEOPLE</h2>
  <div class="person" style="left:68px"><div class="photo" role="img" aria-label="Portrait of team member in a dark suit" style="background:linear-gradient(180deg,#e9ecef,#c9ced4 55%,#2a2f3a)"></div><div class="plate"><b>DANIEL REYES</b><span>Mechanical Engineer</span></div></div>
  <div class="person" style="left:338px"><div class="photo" role="img" aria-label="Portrait of team member in a navy blazer" style="background:linear-gradient(180deg,#e6e8eb,#c4c9cf 55%,#1e2a44)"></div><div class="plate"><b>MARCUS HOLT</b><span>Mechanical Engineer</span></div></div>
  <div class="person" style="left:610px"><div class="photo" role="img" aria-label="Portrait of team member in a grey suit" style="background:linear-gradient(180deg,#b9b3ab,#8c867f 55%,#4a4846)"></div><div class="plate"><b>DANIEL REYES</b><span>Mechanical Engineer</span></div></div>
  <div class="person" style="left:882px"><div class="photo" role="img" aria-label="Portrait of team member in a blue suit" style="background:linear-gradient(180deg,#b8c6d6,#8ea4bd 55%,#294a86)"></div><div class="plate"><b>MARCUS HOLT</b><span>Mechanical Engineer</span></div></div>
  <div class="dots" style="top:710px"><i class="on"></i><i></i><i></i><i></i></div>
</section>

<footer class="site-footer">
  <p class="about">We are Ostrevo. Your<br>Partner in Industrial<br>Safety and Compliance</p>
  <ul class="foot-links">
    <li><i></i>About Us</li>
    <li><i></i>Solutions</li>
    <li><i></i>Articles</li>
    <li><i></i>Contact Us</li>
  </ul>
  <hr>
  <div class="legal">Legal | Cookies | Privacy</div>
  <div class="social"></div>
  <div class="copy">(C) Ostrevo (S) Pte Ltd 2025</div>
  <div class="brand"><span class="mark"></span>OSTREVO</div>
</footer>

</body>
</html>
```